VELMOTIK Amazing Business Cards Challenge

Velmoti is a new technology company that will provide engineering and manufacturing services in the electric vehicle industry.

We are looking at a new business card that will support our orientation in providing advanced, innovative solutions. The business card will be lean and present the only information required to be more efficient.

Target Market(s)

Fleet operators, private commercial vehicle operators, delivery companies.

Industry/Entity Type

Business

Contact Information for Business Card

Use the logo and its colors, use a white background.

Font styles to use
Sans Serif

Colors
0455a3
ffffff
9bcb3c

Requirements
Must have
• Velmotik Logo
• All informations in the DOC file = 3 different cards.
• White background
Nice to have
• Icons for email, phone and web address.
• Cute design and strong identity.
Should not have
• Bleeds

```html
<!DOCTYPE html>
<html lang="fr">
<head>
<meta charset="utf-8">
<title>Velmotik – cartes professionnelles</title>
<link rel="stylesheet" href="https://fonts.googleapis.com/css2?family=Open+Sans:wght@300;400;600&display=swap">
<style>
  :root {
    --stage: #e9e6e1;
    --card: #ffffff;
    --card-edge: #f1f3f5;
    --brand-blue: #1e8fc8;
    --brand-blue-deep: #0f6fa6;
    --ink: #555b62;
    --ink-soft: #7b8188;
    --ghost: #e6ecf2;
  }
  * { box-sizing: border-box; margin: 0; padding: 0; }
  html, body { width: 1200px; height: 600px; overflow: hidden; }
  body {
    background: var(--stage);
    font-family: "Open Sans", Arial, sans-serif;
    color: var(--ink);
    display: flex;
    align-items: center;
    justify-content: center;
    gap: 60px;
  }
  .card {
    position: relative;
    width: 500px;
    height: 286px;
    background: linear-gradient(180deg, var(--card) 0%, var(--card-edge) 100%);
    border-radius: 6px;
    box-shadow: 0 6px 18px rgba(0,0,0,0.12);
    overflow: hidden;
  }
  .band {
    position: absolute;
    top: 0; bottom: 0;
    width: 22px;
    background: var(--brand-blue);
  }
  .band::after {
    content: "";
    position: absolute;
    top: 0; bottom: 0;
    width: 7px;
    background: var(--brand-blue-deep);
  }
  .card--front .band { right: 0; }
  .card--front .band::after { right: 0; }
  .card--back .band { left: 0; }
  .card--back .band::after { left: 0; }

  .ghost-mark {
    position: absolute;
    border-radius: 50%;
    background: var(--ghost);
  }
  .card--front .ghost-mark { width: 130px; height: 130px; right: 110px; top: 20px; }
  .card--back .ghost-mark { width: 170px; height: 170px; left: 165px; top: 58px; }

  .brand {
    position: absolute;
    left: 32px; top: 36px;
    display: flex;
    align-items: center;
    gap: 12px;
  }
  .brand__square {
    width: 30px; height: 30px;
    background: var(--brand-blue);
    border-radius: 3px;
  }
  .brand__name {
    font-size: 32px;
    font-weight: 300;
    color: var(--ink);
    letter-spacing: 1px;
    line-height: 1;
  }

  .web {
    position: absolute;
    display: flex;
    align-items: center;
    gap: 6px;
    font-size: 12px;
    color: var(--ink);
  }
  .card--front .web { right: 40px; top: 28px; }
  .card--back .web { right: 28px; bottom: 24px; }
  .web__dot {
    width: 10px; height: 10px;
    border-radius: 50%;
    background: var(--brand-blue);
  }

  .contact {
    position: absolute;
    left: 32px; top: 128px;
    font-size: 11.5px;
    line-height: 1.45;
  }
  .contact__name {
    font-size: 17px;
    color: var(--brand-blue);
    font-weight: 400;
  }
  .contact__name small {
    font-size: 11px;
    color: var(--ink-soft);
  }
  .contact__role { font-size: 12px; margin-bottom: 12px; }
  .contact__address { margin-bottom: 10px; }
  .contact__address .accent { color: var(--brand-blue); }
  .contact__line {
    display: flex;
    align-items: center;
    gap: 7px;
  }
  .contact__line svg { width: 11px; height: 11px; flex: none; }
</style>
</head>
<body>
  <section class="card card--front" aria-label="Recto de la carte">
    <div class="ghost-mark" aria-hidden="true"></div>
    <div class="band" aria-hidden="true"></div>

    <div class="brand">
      <span class="brand__square" aria-hidden="true"></span>
      <span class="brand__name">velmotik</span>
    </div>

    <div class="web"><span class="web__dot" aria-hidden="true"></span>velmotik.com</div>

    <div class="contact">
      <p class="contact__name">Mathis Durocher<small>, ing., M.Sc.A.</small></p>
      <p class="contact__role">Président | CEO</p>
      <p class="contact__address">410 – 288 Laurier Ouest<br>Montréal <span class="accent">(Québec)</span> H2T 1K9 Canada</p>
      <p class="contact__line">
        <svg viewBox="0 0 12 12" aria-hidden="true"><path d="M2.5 1h2l1 2.8-1.3 1a6 6 0 0 0 3 3l1-1.3L11 7.5v2a1.2 1.2 0 0 1-1.3 1.2A9 9 0 0 1 1.3 2.3 1.2 1.2 0 0 1 2.5 1z" fill="var(--brand-blue)"/></svg>
        +1 514 555 0187
      </p>
      <p class="contact__line">
        <svg viewBox="0 0 12 12" aria-hidden="true"><rect x="0.5" y="2" width="11" height="8" rx="1" fill="var(--brand-blue)"/><path d="M1 2.8l5 3.6 5-3.6" fill="none" stroke="#fff" stroke-width="1"/></svg>
        mdurocher@velmotik.com
      </p>
    </div>
  </section>

  <section class="card card--back" aria-label="Verso de la carte">
    <div class="band" aria-hidden="true"></div>
    <div class="ghost-mark" aria-hidden="true"></div>
    <div class="web"><span class="web__dot" aria-hidden="true"></span>velmotik.com</div>
  </section>
</body>
</html>
```